Harbourline Strategy Group firm

I need a business card that is succint for a Brisbane based business called Harbourline Strategy Group Pty Ltd.
We bridge the gaps between People, Process and Technology.

We are a specialist operational excellence firm, delivering strategic consulting and business advisory services in six core capabilities, across all industries and all business lines to improve performance, efficiency, profitability, automation and scalability, for clients across Australia &New Zealand.
Updates

Hi Designers, I have uploaded the logo in 3D .png format, to assist in card design.

Target Market(s)

Project Management professionals, IT professionals, corporate and government clients managing transitioning or transformation projects.

Contact Information for Business Card

Harbourline Strategy Group Pty Ltd

Daniel Ferreira
Principal Consultant

mobile: +61 417 260 315
email: daniel@harbourlinestrategygroup.com.au
webpage: www.harbourlinestrategygroup.com

professional services: strategic advisors,

Font styles to use
Sans Serif

Requirements
Must have
• Business name: Harbourline Strategy Group
logo: attached
Contact person: Daniel Ferreira
Title: Principal Consultant
contact details:
mobile +61 417 260
email: daniel@HarbourlineStrategyGroup.com.au
website: HarbourlineStrategyGroup.com

on back side with logo include: A.B.N. 58210947362

professional services offered: Business Analysis, Strategic Advisory
Nice to have
• QR code
Should not have
• contacts picture

```html
<!DOCTYPE html>
<html lang="en">
<head>
<meta charset="utf-8">
<title>Harbourline Strategy Group – Business Card</title>
<link href="https://fonts.googleapis.com/css2?family=Roboto+Condensed:wght@400;500;700&family=Bree+Serif&display=swap" rel="stylesheet">
<style>
  :root {
    --navy: #1f2645;
    --red: #e0242a;
    --white: #ffffff;
    --grey-line: #9a9a9a;
    --backdrop: #b9b9b9;
  }
  * { margin: 0; padding: 0; box-sizing: border-box; }
  html, body { width: 1200px; height: 1200px; overflow: hidden; }
  body {
    background: var(--backdrop);
    font-family: "Roboto Condensed", sans-serif;
    position: relative;
  }
  .card {
    position: absolute;
    top: 303px;
    width: 370px;
    height: 594px;
  }
  .card--front {
    left: 200px;
    border-radius: 8px;
    overflow: hidden;
    color: var(--white);
  }
  .front-backdrop {
    position: absolute; inset: 0;
    background: linear-gradient(180deg, #222747 0%, #4a2240 25%, #7d2437 50%, #b5232f 75%, var(--red) 100%);
  }
  .card--back {
    left: 599px;
    width: 364px;
    background: var(--white);
    color: var(--navy);
  }
  .wordmark {
    position: absolute;
    display: flex;
    align-items: center;
    gap: 12px;
    font-family: "Roboto Condensed", sans-serif;
    font-weight: 700;
    text-transform: uppercase;
    line-height: 1;
  }
  .wordmark__square { width: 34px; height: 34px; flex: none; }
  .wordmark__name { font-size: 31px; letter-spacing: 0.5px; }
  .wordmark__name span { display: block; }
  .wordmark__name small { display: block; font-size: 31px; }
  .card--front .wordmark { left: 48px; top: 698px; top: 396px; }
  .card--front .wordmark__square { background: var(--white); }
  .card--back .wordmark { left: 38px; top: 140px; color: var(--navy); }
  .card--back .wordmark__square { background: var(--red); }
  .services {
    position: absolute; left: 0; right: 0; top: 506px;
    text-align: center;
  }
  .services__label { font-size: 17px; letter-spacing: 0.3px; }
  .services__tagline { font-size: 21px; margin-top: 5px; }
  .holder {
    position: absolute; left: 0; right: 0; top: 392px;
    text-align: center;
  }
  .holder__name {
    font-family: "Bree Serif", serif;
    color: var(--red);
    font-size: 24px;
    letter-spacing: 0.5px;
    text-transform: uppercase;
  }
  .holder__title { font-size: 17px; margin-top: 0; }
  .icon-row {
    position: absolute; left: 87px; top: 452px;
    display: flex; align-items: center; gap: 5px;
  }
  .icon-row__rule { width: 52px; height: 1px; background: var(--grey-line); margin: 0 3px; }
  .icon-row svg { display: block; }
  .contacts {
    position: absolute; left: 0; right: 0; top: 488px;
    text-align: center;
    font-size: 17px;
    line-height: 21.5px;
    letter-spacing: 0.2px;
  }
  .contacts .accent { color: var(--red); }
</style>
</head>
<body>
  <section class="card card--front">
    <div class="front-backdrop" role="img" aria-label="Navy to red gradient background"></div>
    <div class="wordmark">
      <div class="wordmark__square"></div>
      <div class="wordmark__name"><span>Harbourline</span><small>Strategy Group</small></div>
    </div>
    <div class="services">
      <p class="services__label">PROFESSIONAL SERVICES</p>
      <p class="services__tagline">strategic advisors</p>
    </div>
  </section>

  <section class="card card--back">
    <div class="wordmark">
      <div class="wordmark__square"></div>
      <div class="wordmark__name"><span>Harbourline</span><small>Strategy Group</small></div>
    </div>
    <div class="holder">
      <h1 class="holder__name">Daniel Ferreira</h1>
      <p class="holder__title">Principal Consultant</p>
    </div>
    <div class="icon-row">
      <div class="icon-row__rule"></div>
      <svg width="25" height="25" viewBox="0 0 25 25" aria-label="Phone">
        <rect width="25" height="25" rx="3" fill="#e0242a"/>
        <path d="M6 10c0-3 13-3 13 0v1.5h-3V10H9v1.5H6z M8 12h9l2 6H6z" fill="#fff"/>
      </svg>
      <svg width="25" height="25" viewBox="0 0 25 25" aria-label="Email">
        <rect width="25" height="25" rx="3" fill="#e0242a"/>
        <rect x="5.5" y="8" width="14" height="10" fill="none" stroke="#fff" stroke-width="1.4"/>
        <path d="M5.5 8l7 5.5 7-5.5 M5.5 18l5-4.5 M19.5 18l-5-4.5" fill="none" stroke="#fff" stroke-width="1.2"/>
      </svg>
      <svg width="25" height="25" viewBox="0 0 25 25" aria-label="Website">
        <rect width="25" height="25" rx="3" fill="#e0242a"/>
        <circle cx="12.5" cy="12.5" r="7" fill="#fff"/>
        <path d="M9 8.5c2 1 1 3 3 3.5s0 3 1.5 4.5M15 7.5c0 2 2 2 3.5 3" fill="none" stroke="#e0242a" stroke-width="1.6"/>
      </svg>
      <div class="icon-row__rule"></div>
    </div>
    <div class="contacts">
      <p>+61 417 260 315</p>
      <p>daniel@harbourlinestrategygroup.com.au</p>
      <p>www.<span class="accent">harbourlinestrategygroup</span>.com</p>
    </div>
  </section>
</body>
</html>
```